Credit card acceptance poster

I need a poster explaining to my customers that the washers and dryers at my laundromat accept credit card payments and most mobile wallet payments. I have attached a flyer I made. It looks terrible so I need help. The cc readers accept: ZELO, TRUVENBANK, ORBINTAL, COLDRIDGE FUNDCO, KIVRA TAP, TREVO WAVE, AND ODELIX SWIPE.

Colors
0054AA
0677BA
7BADD7
CADEEF
E8F1F8

```html
<!DOCTYPE html>
<html lang="en">
<head>
<meta charset="utf-8">
<title>Tidecrest Laundromat – Card Payments Poster</title>
<link rel="stylesheet" href="https://fonts.googleapis.com/css2?family=Anton&family=Bebas+Neue&family=Nunito+Sans:wght@600;800&display=swap">
<style>
  :root {
    --blue-deep: #0054AA;
    --blue-mid: #0677BA;
    --blue-soft: #7BADD7;
    --blue-pale: #CADEEF;
    --blue-mist: #E8F1F8;
    --band-dark: #2f5d94;
    --band-bright: #0d8fd0;
    --ink: #333333;
    --paper: #ffffff;
    --badge-bg: #f1f2f4;
  }
  * { margin: 0; padding: 0; box-sizing: border-box; }
  html, body { width: 988px; height: 1200px; overflow: hidden; background: var(--paper); }
  .poster {
    position: relative; width: 988px; height: 1200px;
    background: var(--paper); overflow: hidden;
    font-family: "Nunito Sans", sans-serif;
  }
  .frame-line {
    position: absolute; left: 28px; top: 33px; right: 28px; bottom: 33px;
    border: 2px solid #3c70b4;
  }
  .hero-photo {
    position: absolute; left: 239px; top: 0; width: 546px; height: 585px;
    background: linear-gradient(180deg, #4a4a4c 0%, #5b5b5e 30%, #d8d4d0 55%, #3a3a3a 68%, #c9733a 78%, #b8652f 100%);
  }
  .headline-top {
    position: absolute; left: 153px; top: 99px; width: 685px; height: 118px;
    background: var(--band-dark); color: var(--paper);
    font-family: "Bebas Neue", sans-serif; font-size: 96px; line-height: 118px;
    text-align: center; letter-spacing: 0.5px;
  }
  .headline-main {
    position: absolute; left: 91px; top: 217px; width: 807px; height: 157px;
    background: var(--band-bright); color: var(--paper);
    font-family: "Anton", sans-serif; font-size: 128px; line-height: 157px;
    text-align: center; letter-spacing: 1px;
    text-shadow: 5px 5px 0 var(--band-dark);
  }
  .accept-pill {
    position: absolute; left: 96px; top: 588px; width: 797px; height: 97px;
    border-radius: 49px;
    background: linear-gradient(90deg, var(--blue-mid), var(--band-dark));
    color: var(--paper); text-align: center;
    font-family: "Bebas Neue", sans-serif; font-size: 84px; line-height: 101px;
    text-shadow: 3px 3px 0 rgba(0,40,90,0.45);
  }
  .accept-copy {
    position: absolute; left: 0; top: 700px; width: 988px;
    text-align: center; color: var(--ink);
    font-weight: 600; font-size: 39px; line-height: 53px;
  }
  .method-group {
    position: absolute; top: 837px; height: 88px;
    background: var(--badge-bg); border-radius: 8px;
    box-shadow: 0 6px 8px rgba(0,0,0,0.08);
    display: flex; align-items: center; justify-content: center; gap: 13px;
  }
  .method-group.cards { left: 93px; width: 450px; }
  .method-group.wallets { left: 552px; width: 344px; }
  .method-badge {
    width: 91px; height: 56px; background: var(--paper);
    border: 2px solid #555; border-radius: 4px;
    display: flex; align-items: center; justify-content: center;
    text-align: center; color: var(--blue-deep);
    font-weight: 800; font-size: 12px; line-height: 14px; padding: 0 3px;
  }
  .splash-area {
    position: absolute; left: 0; bottom: 0; width: 560px; height: 290px;
    background: linear-gradient(160deg, var(--blue-soft) 0%, var(--blue-mid) 60%, var(--blue-deep) 100%);
    border-top-right-radius: 100% 100%;
    opacity: 0.9;
  }
  .splash-corner {
    position: absolute; right: 0; bottom: 0; width: 230px; height: 90px;
    background: linear-gradient(180deg, var(--blue-soft), var(--blue-mid));
    border-top-left-radius: 100% 100%;
  }
  .brand {
    position: absolute; left: 520px; top: 985px; width: 380px;
    color: var(--blue-deep); font-weight: 800;
    display: flex; align-items: center; gap: 14px;
  }
  .brand-dot { width: 30px; height: 30px; border-radius: 50%; background: var(--blue-mid); flex: none; }
  .brand-name { font-size: 44px; line-height: 44px; }
  .brand-name small { display: block; font-size: 25px; line-height: 30px; letter-spacing: 4px; }
</style>
</head>
<body>
<main class="poster">
  <div class="frame-line"></div>
  <div class="hero-photo" role="img" aria-label="Photo of a man in a grey blazer and orange trousers pulling out his empty pockets"></div>
  <h1 class="headline-top">NO BILLS OR COINS?</h1>
  <h2 class="headline-main">NO PROBLEM!</h2>

  <div class="accept-pill">OUR MECHINES ACCEPT</div>
  <p class="accept-copy">Credit Card Payments and<br>Most Mobile Wallet applications.</p>

  <div class="method-group cards">
    <span class="method-badge">ZELO</span>
    <span class="method-badge">TRUVENBANK</span>
    <span class="method-badge">ORBINTAL</span>
    <span class="method-badge">COLDRIDGE FUNDCO</span>
  </div>
  <div class="method-group wallets">
    <span class="method-badge">KIVRA TAP</span>
    <span class="method-badge">TREVO WAVE</span>
    <span class="method-badge">ODELIX SWIPE</span>
  </div>

  <div class="splash-area" role="img" aria-label="Decorative blue water splash illustration"></div>
  <div class="splash-corner" role="img" aria-label="Decorative blue water splash illustration"></div>

  <div class="brand">
    <span class="brand-dot"></span>
    <span class="brand-name">TIDECREST<small>LAUNDROMAT</small></span>
  </div>
</main>
</body>
</html>
```